Website improvements and Adding Functionalities at https://vornet.site/pelmarq

1.Search functionality
2.Payment process functionality
3. Application configuration
4. Registration functionality activation
5. Chat functionality
6.Language switching functionality (Portuguese & French)
7.Bespoke interactive modules
8. Automated web scraping and data synchronisation mechanisms
9. News Page
10.Webinar facilities
11. Basic SEO optimisation
12. Speed and performance optimisation
13. Security configuration
14. Google Analytics integration
15. Cross-browser and mobile testing
16. Website deployment and launch support

Target Market(s)

My target markets are companies, investors, suppliers and professionals with an interest in the Mozambican oil and gas sector

Industry/Entity Type

Oil and Gas

Coding

Coded - Design and coding required

Number of Pages Required

1 page

Requirements
Must have
• Improve the existing page at https://vornet.site/pelmarq and add the following features to it: 1. Search functionality 2. Payment process functionality 3. Application configuration 4. Activation of registration functionality 5. Chat functionality 6. Language switching functionality (Portuguese & French) 7. Bespoke interactive modules 8. Automated web scraping and data synchronisation mechanisms 9. News Page

```html
<!DOCTYPE html>
<html lang="pt">
<head>
<meta charset="utf-8">
<title>Pelmarq — Inteligência da Indústria de Petróleo e Gás</title>
<link href="https://fonts.googleapis.com/css2?family=Barlow+Condensed:wght@600;700&family=Inter:wght@400;500;600&display=swap" rel="stylesheet">
<style>
:root{
  --navy:#211c45;
  --navy-deep:#191536;
  --orange:#ef5f28;
  --orange-light:#f7913a;
  --cream:#fdf5ec;
  --ink:#1f1d2b;
  --muted:#5d5a66;
  --line:#d9d2c8;
  --white:#ffffff;
}
*{box-sizing:border-box;margin:0;padding:0}
html,body{width:1200px;height:5291px;overflow:hidden}
body{font-family:"Inter",sans-serif;color:var(--ink);background:var(--cream);position:relative}
.abs{position:absolute}
h1,h2,h3,.display{font-family:"Barlow Condensed",sans-serif;font-weight:700;text-transform:uppercase;letter-spacing:.3px}
.eyebrow{font-size:11px;color:var(--orange);font-weight:500}
.btn{display:inline-flex;align-items:center;justify-content:center;background:var(--orange);color:#fff;font-family:"Barlow Condensed",sans-serif;font-weight:700;font-size:13px;border-radius:5px;box-shadow:3px 3px 0 #9c3410}
p{font-size:11.5px;line-height:1.5;color:var(--muted)}

/* top bar */
.topbar{left:0;top:0;width:1200px;height:25px;background:var(--navy-deep);color:#fff;font-size:10px}
.topbar .socials{left:125px;top:5px;display:flex;gap:6px}
.dot{width:14px;height:14px;border-radius:50%;border:1px solid #fff}
.topbar .tag{left:0;width:1200px;top:6px;text-align:center}
.topbar .lang{left:980px;top:6px;display:flex;gap:5px;align-items:center}
.topbar .lang i{width:10px;height:10px;border-radius:50%;background:var(--orange);display:inline-block}

/* nav */
.nav{left:0;top:25px;width:1200px;height:57px;background:var(--cream)}
.brand{left:120px;top:28px;width:135px;height:78px;background:var(--cream);border-radius:0 0 8px 8px;z-index:3;display:flex;flex-direction:column;align-items:center;justify-content:center;gap:4px}
.brand .mark{width:26px;height:26px;border-radius:50%;background:var(--navy)}
.brand span{font-family:"Barlow Condensed",sans-serif;font-weight:700;font-size:15px;color:var(--navy)}
.menu{left:257px;display:flex;gap:17px;font-size:10.5px;color:var(--ink)}
.nav .cta{left:982px;width:94px;height:32px;background:var(--navy);color:#fff;border-radius:4px;font-size:11px;display:flex;align-items:center;justify-content:center}

/* hero */
.hero{left:0;top:82px;width:1200px;height:592px;border-radius:0 0 34px 34px;overflow:hidden;background:linear-gradient(100deg,#2a2150 0%,#3b2a55 40%,#8d4a3f 70%,#c86a3c 100%)}
.hero .photo{inset:0}
.search{left:125px;top:118px;width:302px;height:30px;border-radius:15px;background:rgba(255,255,255,.12);color:#ddd;font-size:10px;display:flex;align-items:center;gap:8px;padding-left:14px}
.hero h1{left:125px;top:160px;width:560px;font-size:40px;line-height:44px;color:#fff}
.hero p{left:125px;top:302px;width:560px;color:#eee;font-size:11.5px}
.hero .btn{left:125px;top:374px;width:140px;height:34px}
.hero .thumb-label{left:357px;top:432px;font-size:10px;color:#fff}
.hero .thumb{left:357px;top:450px;width:213px;height:120px;border-radius:4px;background:linear-gradient(180deg,#e8b07a,#6a6aa0 60%,#2d3f6a)}
.tabs{left:125px;top:554px;width:950px;display:flex;justify-content:space-between}
.tabs div{width:215px;font-size:10.5px;color:#fff;padding-bottom:8px;border-bottom:1px solid rgba(255,255,255,.6)}
.chat{left:1094px;top:468px;width:52px;height:52px;border-radius:50%;background:#f3ece4;display:flex;align-items:center;justify-content:center}

/* about */
.about-img{left:125px;top:760px;width:331px;height:356px;border-radius:8px;background:linear-gradient(160deg,#e0a56a,#7b5b4e 55%,#34324a)}
.about .eyebrow{left:490px;top:766px}
.about h2{left:490px;top:786px;width:560px;font-size:37px;line-height:42px;color:var(--navy)}
.about .p1{left:490px;top:888px;width:580px}
.about .p2{left:490px;top:944px;width:580px}
.about .btn{left:490px;top:1070px;width:145px;height:38px}
.wordmark{left:720px;top:1120px;font-size:90px;line-height:90px;color:rgba(33,28,69,.18);white-space:nowrap}

/* stats */
.stats{left:0;top:1202px;width:1200px;height:308px;background:linear-gradient(90deg,var(--navy) 40%,#34305e 75%,#5b4a6a)}
.stats h2{left:125px;top:78px;width:380px;font-size:27px;line-height:30px;color:#fff}
.stat{top:138px;width:185px;color:#fff;border-bottom:1px solid rgba(255,255,255,.5);padding-bottom:28px}
.stat b{display:block;font-weight:400;font-size:38px;line-height:40px}
.stat span{font-size:11px;color:#ddd}

/* platform */
.platform .eyebrow{left:125px;top:1580px}
.platform h2{left:125px;top:1605px;width:420px;font-size:37px;line-height:44px;color:var(--navy)}
.platform p{left:646px;top:1628px;width:430px}
.card{top:1738px;height:245px;border-radius:6px;overflow:hidden;border:1px solid #e2c8a8}
.card .fill{position:absolute;inset:0}
.card .cap{position:absolute;left:12px;bottom:16px;right:12px;color:#fff;font-family:"Barlow Condensed",sans-serif;font-weight:700;font-size:13px}
.card .cap small{display:block;font-family:"Inter",sans-serif;font-weight:400;font-size:10px;line-height:1.45;color:#ddd;margin-top:4px}
.platform .btn{left:528px;top:2024px;width:143px;height:40px}

/* how */
.how{left:0;top:2110px;width:1200px;height:444px;background:var(--navy)}
.how .eyebrow{left:0;width:1200px;text-align:center;top:64px}
.how h2{left:0;width:1200px;text-align:center;top:84px;font-size:37px;color:#fff}
.how p{left:170px;width:860px;text-align:center;top:130px;color:#ddd}
.step{top:228px;width:200px;text-align:center;color:#fff}
.step .num{font-family:"Barlow Condensed",sans-serif;font-weight:700;font-size:18px;color:var(--orange);line-height:20px}
.step .badge{width:92px;height:92px;margin:4px auto 0;border-radius:50%;background:#fff;display:flex;align-items:center;justify-content:center}
.step .lab{margin-top:12px;font-family:"Barlow Condensed",sans-serif;font-weight:700;font-size:13px;line-height:16px}
.arrow{top:282px;width:110px;height:12px}

/* advantage */
.adv{left:0;top:2554px;width:1200px;height:600px;background:linear-gradient(180deg,#ebe6ef,#e4e0ec)}
.adv .eyebrow{left:125px;top:76px}
.adv h2{left:125px;top:100px;width:460px;font-size:37px;line-height:44px;color:var(--navy)}
.adv .lead{left:618px;top:128px;width:460px}
.feat{left:125px;width:380px;display:flex;gap:40px}
.feat .ic{width:56px;height:56px;border-radius:50%;background:var(--navy);flex:none;display:flex;align-items:center;justify-content:center}
.feat h3{font-family:"Inter",sans-serif;text-transform:none;font-size:12px;font-weight:600;color:var(--navy);margin-bottom:3px;letter-spacing:0}
.feat p{font-size:11px}
.book{left:596px;top:250px;width:470px;height:365px;border-radius:10px;background:linear-gradient(150deg,#2a3a78,#1a2350 60%,#3a3550)}

/* news */
.news .eyebrow{left:125px;top:3222px}
.news h2{left:125px;top:3245px;width:460px;font-size:37px;line-height:44px;color:var(--navy)}
.news .lead{left:705px;top:3273px;width:370px}
.ncard{top:3376px;width:310px}
.ncard .im{height:222px;border-radius:4px}
.ncard h4{font-size:12px;font-weight:500;color:var(--ink);margin:18px 6px 0;line-height:1.4}
.ncard h4 em{font-style:normal;color:var(--orange);font-size:10px}
.ncard .date{margin:26px 6px 0;font-size:10.5px;color:var(--muted);padding-bottom:8px;border-bottom:1px solid var(--line)}
.news .btn{left:528px;top:3734px;width:143px;height:40px}

/* webinars */
.web .eyebrow{left:125px;top:3893px}
.web h2{left:125px;top:3916px;width:460px;font-size:37px;line-height:44px;color:var(--navy)}
.web .lead{left:628px;top:3924px;width:450px}
.wcard{top:4030px;height:350px;border-radius:8px;overflow:hidden}
.wcard .cap{position:absolute;left:30px;right:30px;bottom:30px;color:#fff}
.wcard .cap h3{font-size:17px;margin-bottom:4px}
.wcard .cap p{color:#ddd;font-size:11px}

/* sign-up */
.cta-photo{left:0;top:4438px;width:520px;height:535px;background:linear-gradient(180deg,#d98b4f,#6b3d3f 55%,#241d3c)}
.cta-panel{left:440px;top:4438px;width:760px;height:535px;border-radius:40px;background:linear-gradient(120deg,var(--orange),var(--orange-light))}
.form h2{left:560px;top:4518px;font-size:37px;color:#fff}
.form p{left:560px;top:4568px;width:520px;color:#fff}
.field{height:34px;border:1px solid rgba(255,255,255,.8);border-radius:4px;color:#fff;font-size:10.5px;padding:10px 12px}
.form .btn{left:560px;top:4815px;width:145px;height:40px;background:#fff;color:var(--orange);box-shadow:3px 3px 0 #a8401a}

/* footer */
.footer{left:0;top:4973px;width:1200px;height:318px;background:var(--navy)}
.footer .fbrand{left:125px;top:36px;display:flex;align-items:center;gap:10px}
.footer .fbrand i{width:30px;height:30px;border-radius:50%;background:#f3ece4}
.footer .fbrand span{font-family:"Barlow Condensed",sans-serif;font-weight:700;font-size:20px;color:#fff}
.footer .desc{left:125px;top:122px;width:290px;color:#ddd;font-size:10.5px}
.footer .soc{left:125px;top:222px;display:flex;gap:10px}
.footer .soc .dot{width:18px;height:18px}
.footer h5{font-size:10px;color:#fff;font-weight:600;margin-bottom:12px}
.footer ul{list-style:none;font-size:10.5px;color:#ddd;line-height:17px}
.contact li{display:flex;gap:12px;align-items:flex-start;margin-bottom:12px}
.contact svg{flex:none}
.footer .copy{left:0;top:288px;width:1200px;text-align:center;color:#ccc;font-size:10px}
.footer .rule{left:125px;top:272px;width:950px;height:1px;background:rgba(255,255,255,.2)}
.vline{left:468px;top:50px;width:1px;height:200px;background:rgba(255,255,255,.2)}
</style>
</head>
<body>

<div class="abs topbar">
  <div class="abs tag">Trusted Source for Mozambique's Oil &amp; Gas Industry Intelligence</div>
  <div class="abs socials"><span class="dot"></span><span class="dot"></span><span class="dot"></span></div>
  <div class="abs lang"><i></i>Portuguese ▾</div>
</div>

<header class="abs nav">
  <nav class="abs menu" style="top:23px">
    <span>Início</span><span>Análises do Setor</span><span>Oportunidades em Petróleo &amp; Gás</span><span>Rede de Fornecedores &amp; Empresas</span><span>Registar</span><span>Quadro Legal</span>
  </nav>
  <div class="abs cta" style="top:13px">Contacte-Nos</div>
</header>
<div class="abs brand"><div class="mark"></div><span>PELMARQ</span></div>

<section class="abs hero">
  <div class="abs photo" role="img" aria-label="Plataforma petrolífera offshore ao pôr do sol"></div>
  <div class="abs search">
    <svg width="11" height="11" viewBox="0 0 12 12"><circle cx="5" cy="5" r="4" fill="none" stroke="#fff" stroke-width="1.4"/><path d="M8 8l3 3" stroke="#fff" stroke-width="1.4"/></svg>
    Encontre exatamente o que precisa...
  </div>
  <h1 class="abs">Aceda à inteligência da indústria de petróleo e gás de Moçambique numa só plataforma</h1>
  <p class="abs">Pelmarq é uma plataforma moderna de conexão e consultoria online, concebida para facilitar o acesso à indústria de Petróleo e Gás de Moçambique através de informações premium do setor, dados de fornecedores, concursos, quadros legais e dados estratégicos de projetos.</p>
  <div class="abs btn">Registe-se Agora</div>
  <div class="abs thumb-label">Informações sobre Hidrocarbonetos</div>
  <div class="abs thumb" role="img" aria-label="Plataforma de hidrocarbonetos no mar"></div>
  <div class="abs tabs">
    <div>Quadro Legal de Conteúdo Local</div>
    <div style="border-color:transparent"></div>
    <div>Propriedade &amp; Acesso em P&amp;G</div>
    <div>Livros sobre Petróleo &amp; Gás Moçambicano</div>
  </div>
  <div class="abs chat">
    <svg width="26" height="26" viewBox="0 0 26 26"><circle cx="13" cy="13" r="12" fill="var(--orange)"/><path d="M7 9h12v7h-7l-3 3v-3H7z" fill="#fff"/></svg>
  </div>
</section>

<section class="about">
  <div class="abs about-img" role="img" aria-label="Técnicos de petróleo e gás a trabalhar numa instalação industrial"></div>
  <div class="abs eyebrow">O que é Pelmarq?</div>
  <h2 class="abs">Impulsionando o conhecimento.<br>Ligando oportunidades.</h2>
  <p class="abs p1">Pelmarq é uma plataforma moderna de conexão e consultoria online, concebida para facilitar o acesso à indústria de Petróleo e Gás de Moçambique através de informações premium do setor, dados de fornecedores, concursos, quadros legais e dados estratégicos de projetos.</p>
  <p class="abs p2">Através de uma plataforma segura baseada em subscrição, os utilizadores têm acesso a inteligência de mercado selecionada, notícias do setor, perfis de empresas, atualizações de projetos, diretórios de fornecedores, webinars e recursos exclusivos — tudo num único centro centralizado. Pelmarq capacita os utilizadores com informações precisas e atualizadas que apoiam decisões informadas, fortalecem conexões na indústria e ajudam a identificar novas oportunidades de negócio no dinâmico setor energético de Moçambique.</p>
  <div class="abs btn">Explorar Sobre Nós</div>
  <div class="abs display wordmark">PELMARQ CO</div>
</section>

<section class="abs stats">
  <div class="abs" style="left:560px;top:0;width:640px;height:308px;background:linear-gradient(90deg,rgba(33,28,69,0),rgba(120,90,110,.5))" role="img" aria-label="Plataforma petrolífera ao entardecer"></div>
  <h2 class="abs">Confiado pela comunidade de petróleo e gás</h2>
  <div class="abs stat" style="left:125px"><b>5,000+</b><span>Membros Registados</span></div>
  <div class="abs stat" style="left:380px"><b>800+</b><span>Empresas do Setor</span></div>
  <div class="abs stat" style="left:635px"><b>2,500+</b><span>Recursos do Setor</span></div>
  <div class="abs stat" style="left:890px"><b>100+</b><span>Webinars e Eventos</span></div>
</section>

<section class="platform">
  <div class="abs eyebrow">O que irá aceder</div>
  <h2 class="abs">Tudo o que precisa<br>numa só plataforma</h2>
  <p class="abs">Aceda a uma coleção abrangente de inteligência do setor, análises de mercado, recursos empresariais e ferramentas exclusivas concebidas para o manter informado, conectado e competitivo no setor de Petróleo &amp; Gás de Moçambique.</p>
  <div class="abs card" style="left:125px;width:207px"><div class="fill" role="img" aria-label="Profissional a analisar documentos" style="background:linear-gradient(180deg,#c48a5a,#6d4a3a)"></div><div class="cap">Propriedade &amp; Acesso</div></div>
  <div class="abs card" style="left:342px;width:206px"><div class="fill" role="img" aria-label="Engenheiros numa instalação de gás" style="background:linear-gradient(180deg,#d39058,#7a4f36)"></div><div class="cap">Principais Projetos de Gás</div></div>
  <div class="abs card" style="left:560px;width:330px"><div class="fill" role="img" aria-label="Plataforma offshore ao pôr do sol" style="background:linear-gradient(180deg,#e0b08a,#4b4a72 55%,#1f2346)"></div><div class="cap">Base de Dados de Fornecedores &amp; Empresas<small>Empresas moçambicanas capazes de cumprir os requisitos de fornecimento Nível 3.</small></div></div>
  <div class="abs card" style="left:902px;width:205px"><div class="fill" role="img" aria-label="Profissional junto a instalação industrial" style="background:linear-gradient(180deg,#e2a26a,#7d5238)"></div><div class="cap">Contactos da Indústria</div></div>
  <div class="abs card" style="left:1115px;width:100px"><div class="fill" role="img" aria-label="Edifício empresarial" style="background:linear-gradient(180deg,#e6e2d6,#a59b80)"></div><div class="cap">Oportunidades</div></div>
  <div class="abs btn">View All Access</div>
</section>

<section class="abs how">
  <div class="abs eyebrow">O Nosso Processo</div>
  <h2 class="abs">Como funciona a plataforma</h2>
  <p class="abs">A plataforma funciona através de um sistema de pagamento automático seguro que concede aos utilizadores registados acesso a conteúdos premium e exclusivos. Ao subscrever, os utilizadores recebem informações organizadas do setor, concebidas para poupar tempo, melhorar o acesso ao mercado e apoiar o crescimento estratégico dos negócios no setor energético de Moçambique.</p>

  <div class="abs step" style="left:83px"><div class="num">01</div>
    <div class="badge"><svg width="40" height="40" viewBox="0 0 40 40"><circle cx="20" cy="13" r="7" fill="var(--navy)"/><path d="M7 35c2-9 7-13 13-13s11 4 13 13z" fill="var(--navy)"/></svg></div>
    <div class="lab">Crie a Sua Conta</div></div>
  <div class="abs step" style="left:345px"><div class="num">02</div>
    <div class="badge"><svg width="40" height="40" viewBox="0 0 40 40"><rect x="10" y="4" width="20" height="32" rx="3" fill="none" stroke="var(--navy)" stroke-width="3"/><path d="M15 20l4 4 7-8" stroke="var(--navy)" stroke-width="3" fill="none"/></svg></div>
    <div class="lab">Escolha a Sua Subscrição</div></div>
  <div class="abs step" style="left:620px"><div class="num">03</div>
    <div class="badge"><svg width="40" height="40" viewBox="0 0 40 40"><rect x="8" y="17" width="24" height="20" rx="3" fill="var(--navy)"/><path d="M13 17v-6a7 7 0 0114 0v6" stroke="var(--navy)" stroke-width="3" fill="none"/><circle cx="20" cy="26" r="3" fill="#fff"/></svg></div>
    <div class="lab">Desbloqueie Acesso<br>Premium</div></div>
  <div class="abs step" style="left:897px"><div class="num">04</div>
    <div class="badge"><svg width="40" height="40" viewBox="0 0 40 40"><circle cx="20" cy="8" r="6" fill="var(--navy)"/><circle cx="7" cy="32" r="6" fill="var(--navy)"/><circle cx="33" cy="32" r="6" fill="var(--navy)"/><path d="M20 14v8M7 26v-5h26v5" stroke="var(--navy)" stroke-width="2.5" fill="none"/></svg></div>
    <div class="lab">Mantenha-se Conectado &amp;<br>Informado</div></div>

  <svg class="abs arrow" style="left:250px" viewBox="0 0 110 12"><path d="M0 6h100" stroke="var(--orange)" stroke-dasharray="4 4"/><path d="M100 1l7 5-7 5z" fill="var(--orange)"/></svg>
  <svg class="abs arrow" style="left:517px" viewBox="0 0 110 12"><path d="M0 6h100" stroke="var(--orange)" stroke-dasharray="4 4"/><path d="M100 1l7 5-7 5z" fill="var(--orange)"/></svg>
  <svg class="abs arrow" style="left:790px" viewBox="0 0 110 12"><path d="M0 6h100" stroke="var(--orange)" stroke-dasharray="4 4"/><path d="M100 1l7 5-7 5z" fill="var(--orange)"/></svg>
</section>

<section class="abs adv">
  <div class="abs eyebrow">Por que o Pelmarq é Único</div>
  <h2 class="abs">A sua vantagem<br>competitiva começa aqui</h2>
  <p class="abs lead">Descubra as funcionalidades e benefícios que fazem do Pelmarq a plataforma de confiança para inteligência do setor, conexões empresariais e oportunidades no setor de Petróleo &amp; Gás em Moçambique.</p>
  <div class="abs feat" style="top:250px"><div class="ic"><svg width="24" height="24" viewBox="0 0 24 24"><circle cx="12" cy="12" r="9" fill="none" stroke="var(--orange)" stroke-width="2"/><path d="M12 7v5l3 3" stroke="var(--orange)" stroke-width="2" fill="none"/></svg></div>
    <div><h3>Inteligência do Setor Atualizada</h3><p>Receba atualizações frequentes sobre desenvolvimentos no setor de Petróleo &amp; Gás em Moçambique.</p></div></div>
  <div class="abs feat" style="top:355px"><div class="ic"><svg width="24" height="24" viewBox="0 0 24 24"><rect x="5" y="3" width="14" height="18" rx="2" fill="var(--orange)"/><path d="M8 8h8M8 12h8M8 16h5" stroke="var(--navy)" stroke-width="1.6"/></svg></div>
    <div><h3>Informação Curada de Alta Qualidade</h3><p>Aceda a informação cuidadosamente selecionada e sintetizada, adaptada aos intervenientes do setor.</p></div></div>
  <div class="abs feat" style="top:460px"><div class="ic"><svg width="24" height="24" viewBox="0 0 24 24"><circle cx="12" cy="12" r="8" fill="none" stroke="var(--orange)" stroke-width="2"/><path d="M12 6v6h5" stroke="var(--orange)" stroke-width="2" fill="none"/></svg></div>
    <div><h3>Acesso que Poupa Tempo</h3><p>Evite perder horas a procurar em fontes online dispersas com conteúdo organizado e acessível numa única plataforma.</p></div></div>
  <div class="abs book" role="img" aria-label="Livro sobre conteúdo local no setor de petróleo e gás de Moçambique"></div>
</section>

<section class="news">
  <div class="abs eyebrow">Últimas Notícias do Setor</div>
  <h2 class="abs">Notícias de energia e<br>inteligência de mercado</h2>
  <p class="abs lead">Leia as últimas notícias, desenvolvimentos de projetos, atualizações políticas, anúncios de investimento e análises de mercado de fontes confiáveis do setor — tudo num só lugar.</p>
  <article class="abs ncard" style="left:125px"><div class="im" role="img" aria-label="Plataforma offshore de gás ao pôr do sol" style="background:linear-gradient(180deg,#e9a865,#8a5a4a 55%,#2c2c48)"></div>
    <h4>Novo Projeto Offshore de Gás Avança para a Fase de Desenvolvimento... <em>Ler Mais</em></h4><div class="date">25 de Junho de 2026 • 10:30</div></article>
  <article class="abs ncard" style="left:445px"><div class="im" role="img" aria-label="Engenheiros com tablet numa instalação de gás" style="background:linear-gradient(180deg,#a9bcd0,#6c7684 55%,#3e3e4a)"></div>
    <h4>Governo Anuncia Novo Quadro de Investimento em Energia... <em>Ler Mais</em></h4><div class="date">22 de Junho de 2026 • 14:15</div></article>
  <article class="abs ncard" style="left:765px"><div class="im" role="img" aria-label="Profissional observa uma refinaria" style="background:linear-gradient(180deg,#c7d3e0,#6b7a8c 55%,#2f3340)"></div>
    <h4>Líderes do Setor Discutem Futuras Oportunidades Energéticas... <em>Ler Mais</em></h4><div class="date">18 de Junho de 2026 • 09:00</div></article>
  <div class="abs btn">Ver Todas as Notícias</div>
</section>

<section class="web">
  <div class="abs eyebrow">Facilidades de Webinar</div>
  <h2 class="abs">Webinars e<br>eventos do setor</h2>
  <p class="abs lead">Aceda a webinars exclusivos e eventos virtuais onde profissionais do setor partilham insights especializados, inteligência de mercado, melhores práticas e oportunidades emergentes no dinâmico setor de Petróleo &amp; Gás de Moçambique.</p>
  <div class="abs wcard" style="left:125px;width:608px;background:linear-gradient(180deg,#b9b6ae,#5e5a52 55%,#2a2620)" role="img" aria-label="Especialistas a rever planos numa instalação">
    <div class="cap"><h3>Webinars ao Vivo com Especialistas</h3><p>Participe em apresentações ao vivo com líderes do setor que discutem tendências atuais, tecnologias e oportunidades de mercado.</p></div></div>
  <div class="abs wcard" style="left:752px;width:323px;background:linear-gradient(180deg,#c6d3e2,#55637a 55%,#23283a)" role="img" aria-label="Técnicos numa refinaria">
    <div class="cap"><h3>Aprendizagem On-Demand</h3><p>Assista a sessões gravadas de webinars a qualquer momento e reveja discussões valiosas do setor sempre que precisar.</p></div></div>
</section>

<section class="form">
  <div class="abs cta-photo" role="img" aria-label="Plataforma petrolífera ao pôr do sol"></div>
  <div class="abs cta-panel"></div>
  <h2 class="abs">Crie a sua conta</h2>
  <p class="abs">Preencha o formulário abaixo para se registar e obter acesso aos recursos do Pelmarq, redes de fornecedores e oportunidades de negócio no setor de Petróleo &amp; Gás em Moçambique.</p>
  <div class="abs field" style="left:560px;top:4645px;width:252px">Nome Completo</div>
  <div class="abs field" style="left:822px;top:4645px;width:253px">Nome da Empresa</div>
  <div class="abs field" style="left:560px;top:4690px;width:252px">Número de Telefone</div>
  <div class="abs field" style="left:822px;top:4690px;width:253px">Email</div>
  <div class="abs field" style="left:560px;top:4735px;width:515px;height:66px">Mensagem</div>
  <div class="abs btn">Registe-se Agora</div>
</section>

<footer class="abs footer">
  <div class="abs fbrand"><i></i><span>PELMARQ</span></div>
  <p class="abs desc">Pelmarq é uma plataforma digital segura que oferece inteligência premium do setor, análises de mercado, recursos empresariais e oportunidades de networking para profissionais do setor de Petróleo &amp; Gás em Moçambique.</p>
  <div class="abs soc"><span class="dot"></span><span class="dot"></span><span class="dot"></span></div>
  <div class="abs vline"></div>
  <div class="abs" style="left:530px;top:50px"><h5>Quick Links</h5>
    <ul><li>Início</li><li>Análises do Setor</li><li>Oportunidades em Petróleo &amp; Gás</li><li>Rede de Fornecedores &amp; Empresas</li><li>Registar</li><li>Quadro Legal</li><li>Contacte-Nos</li></ul></div>
  <div class="abs" style="left:855px;top:50px"><h5>Contact Us</h5>
    <ul class="contact">
      <li><svg width="18" height="18" viewBox="0 0 18 18"><circle cx="9" cy="9" r="8.5" fill="none" stroke="#fff"/><path d="M9 4a3 3 0 013 3c0 2-3 6-3 6s-3-4-3-6a3 3 0 013-3z" fill="#fff"/></svg><span>Rua das Acácias, 12,<br>Bairro Central, Maputo, Moçambique</span></li>
      <li><svg width="18" height="18" viewBox="0 0 18 18"><circle cx="9" cy="9" r="8.5" fill="none" stroke="#fff"/><path d="M6 5l2 0 1 2-1 1c.5 1 1.5 2 2.5 2.5l1-1 2 1v2c-4 0-7.5-3.5-7.5-7.5z" fill="#fff"/></svg><span>+258 84 000 1122</span></li>
      <li><svg width="18" height="18" viewBox="0 0 18 18"><circle cx="9" cy="9" r="8.5" fill="none" stroke="#fff"/><rect x="5" y="6" width="8" height="6" fill="none" stroke="#fff"/><path d="M5 6l4 3 4-3" stroke="#fff" fill="none"/></svg><span>contacto@pelmarq.site</span></li>
      <li><svg width="18" height="18" viewBox="0 0 18 18"><circle cx="9" cy="9" r="8.5" fill="none" stroke="#fff"/><circle cx="9" cy="9" r="4" fill="none" stroke="#fff"/><path d="M5 9h8M9 5v8" stroke="#fff"/></svg><span>vornet.site/pelmarq</span></li>
    </ul></div>
  <div class="abs rule"></div>
  <div class="abs copy">© 2026 by Pelmarq Co. All Rights Reserved.</div>
</footer>

</body>
</html>
```